Upsell Vertical Banner Ad Design For B2B Marketing Agency Vertical 768px × 1180px IS THE SIZE

I need a banner made for my website www.brightlanepromotionhub.biz This banner will be an upsell advertisement for after someone signs up for my monthly program. When they login to their account for the 1st time I will give them the chance to upgrade their account to our annual program with just one click.

this is a page that upsells it currently to give you an idea how we market ourselves:
https://tlpx.pagevault-example.com/page/tlp-annual-upsell

Use this content:

Are You Ready To Commit To Taking Your Business To The Next Level?

Because We're In This For The Long-Haul and Dedicated To Your Success...

Save $300 By Upgrading To An Annual Membership And Pay Only $74/mth

((BUTTON))Yes, Upgrade My Plan Right Now!

*Must prepay the full year at only $898/yr!

Target Market(s)

business owners

Industry/Entity Type

Marketing

Requirements
Must have
• 768px × 1180px IS THE SIZE vertical

Use this content:

Nice to have
• Use this content:

Should not have
• Use this content:

```html
<!DOCTYPE html>
<html lang="en">
<head>
<meta charset="utf-8">
<title>Bright Lane Promotion Hub – Annual Upgrade</title>
<link href="https://fonts.googleapis.com/css2?family=Montserrat:wght@400;500;600;700&family=Open+Sans:wght@400;600&display=swap" rel="stylesheet">
<style>
  :root {
    --blue-deep: #0d4f9e;
    --blue-main: #1466c1;
    --blue-light: #2a7fd6;
    --white: #ffffff;
    --white-soft: #e8f1fb;
    --green: #43b02a;
    --green-dark: #2f8f1c;
    --grey: #8a8f96;
    --photo-light: #d9d6d0;
    --photo-mid: #8b8680;
    --photo-dark: #4b4642;
  }
  * { box-sizing: border-box; margin: 0; padding: 0; }
  html, body { width: 783px; height: 1200px; overflow: hidden; background: var(--white); }
  .banner {
    position: relative;
    width: 783px;
    height: 1200px;
    font-family: "Montserrat", "Open Sans", sans-serif;
    background: var(--white);
    overflow: hidden;
  }
  .hero-photo {
    position: absolute;
    left: 0; top: 0;
    width: 783px; height: 600px;
    background:
      radial-gradient(ellipse at 62% 30%, #f4f3f1 0%, rgba(244,243,241,0) 45%),
      linear-gradient(160deg, var(--photo-light) 0%, var(--photo-mid) 55%, var(--photo-dark) 100%);
  }
  .panel {
    position: absolute;
    left: 0; top: 0;
    width: 783px; height: 1150px;
  }
  .brand {
    position: absolute;
    top: 612px;
    left: 0; width: 783px;
    display: flex;
    justify-content: center;
    align-items: center;
    gap: 16px;
    color: var(--white);
  }
  .brand-mark {
    width: 46px; height: 46px;
    border-radius: 50%;
    background: var(--white);
  }
  .brand-name {
    font-weight: 600;
    font-size: 26px;
    letter-spacing: 2px;
    text-transform: uppercase;
    line-height: 1.15;
  }
  .benefits {
    position: absolute;
    top: 726px;
    left: 88px;
    width: 625px;
    list-style: none;
  }
  .benefit {
    display: flex;
    align-items: flex-start;
    gap: 22px;
    color: var(--white);
    font-weight: 600;
    font-size: 22px;
    line-height: 30px;
    margin-bottom: 44px;
  }
  .benefit svg { flex: 0 0 26px; margin-top: 2px; }
  .cta {
    position: absolute;
    top: 1036px;
    left: 196px;
    width: 391px;
    height: 60px;
    border-radius: 30px;
    background: linear-gradient(180deg, var(--green) 0%, var(--green-dark) 100%);
    color: var(--white);
    font-weight: 600;
    font-size: 19px;
    letter-spacing: 0.5px;
    text-transform: uppercase;
    display: flex;
    align-items: center;
    justify-content: center;
    box-shadow: 0 3px 6px rgba(0,0,0,0.25);
  }
  .fine-print {
    position: absolute;
    top: 1116px;
    left: 0; width: 783px;
    text-align: center;
    color: var(--white);
    font-family: "Open Sans", sans-serif;
    font-weight: 600;
    font-size: 13px;
    text-transform: uppercase;
    letter-spacing: 0.3px;
  }
  .version-tag {
    position: absolute;
    right: 26px;
    bottom: 14px;
    color: var(--grey);
    font-family: "Open Sans", sans-serif;
    font-size: 12px;
  }
</style>
</head>
<body>
<main class="banner">
  <div class="hero-photo" role="img" aria-label="Photo of a person working on a laptop showing bar and pie charts on a desk with printed reports"></div>

  <svg class="panel" viewBox="0 0 783 1150" width="783" height="1150" aria-hidden="true">
    <defs>
      <linearGradient id="panelFill" x1="0" y1="0" x2="0" y2="1">
        <stop offset="0" stop-color="var(--blue-light)"/>
        <stop offset="0.5" stop-color="var(--blue-main)"/>
        <stop offset="1" stop-color="var(--blue-deep)"/>
      </linearGradient>
    </defs>
    <path d="M0 500 Q392 620 783 470 L783 600 L0 600 Z" fill="var(--white)"/>
    <path d="M0 548 Q392 640 783 520 L783 1150 L0 1150 Z" fill="url(#panelFill)"/>
  </svg>

  <div class="brand">
    <span class="brand-mark"></span>
    <span class="brand-name">Bright Lane<br>Promotion Hub</span>
  </div>

  <ul class="benefits">
    <li class="benefit">
      <svg width="26" height="26" viewBox="0 0 26 26"><circle cx="13" cy="13" r="11" fill="none" stroke="var(--white)" stroke-width="2"/><path d="M8 13.5l3.5 3.5L18 10" fill="none" stroke="var(--white)" stroke-width="2.2" stroke-linecap="round" stroke-linejoin="round"/></svg>
      <span>Are You Ready To Commit To Taking Your Business To The Next Level?</span>
    </li>
    <li class="benefit">
      <svg width="26" height="26" viewBox="0 0 26 26"><circle cx="13" cy="13" r="11" fill="none" stroke="var(--white)" stroke-width="2"/><path d="M8 13.5l3.5 3.5L18 10" fill="none" stroke="var(--white)" stroke-width="2.2" stroke-linecap="round" stroke-linejoin="round"/></svg>
      <span>Because We're In This For The Long-Haul and Dedicated To Your Success...</span>
    </li>
    <li class="benefit">
      <svg width="26" height="26" viewBox="0 0 26 26"><circle cx="13" cy="13" r="11" fill="none" stroke="var(--white)" stroke-width="2"/><path d="M8 13.5l3.5 3.5L18 10" fill="none" stroke="var(--white)" stroke-width="2.2" stroke-linecap="round" stroke-linejoin="round"/></svg>
      <span>Save $300 By Upgrading To An Annual Membership And Pay Only $74/mth</span>
    </li>
  </ul>

  <div class="cta">Yes, Upgrade My Plan Right Now!</div>
  <p class="fine-print">*Must prepay the full year at only $898/yr!</p>
  <span class="version-tag">C2</span>
</main>
</body>
</html>
```